依頼詳細
自宅看板への設置、近隣への配布、楽器屋さんへ置かせて頂くことを想定しています。
ターゲットは幼稚園〜小学生のお母様から年配の方まで幅広く考えたいです。
子供を通わせたくなるような温かみのある可愛らしい雰囲気のチラシにして頂きたいです。
教室名も考えたのですが「藤堂さやか箏・三絃教室」だと長いので、私が教えるということと箏・三絃の教室ということが良い感じに伝わればと思います…
可能であれば公式TALKUとPictogramのQRを貼って頂きたいです。
記載項目
講師名 藤堂(浅野)さやか

講師プロフィール

藤堂(浅野)さやか

埼玉県川越市出身

桐谷学院中学・高等学校卒業
南海芸術大学 音楽学部邦楽科 箏曲生田流専攻卒業

3歳より箏、16歳より三絃を始める
これまでに箏・三絃・十七絃を松田ゆう、村岡千尋子、古畑智代乃の各師に師事

第25回 若人和楽器コンテスト 優良賞・リスナー賞
第4回 北陸古典芸術次世代コンテスト 技能賞

音楽療法・音楽教育・音楽療育なども勉強中
和楽器をもっと身近に。沢山の出会いを大切に楽しみに?

川越教室 : 埼玉県川越市柏原台3-7-5
駐車場あり
守谷教室 : 茨城県守谷市さくら坂5-21-9
駐車場あり

お問い合わせ電話番号 : 080-3917-2586
Pictogram:sayakakotonote

料金 : 30分月4回8000円〜
教材費別途

体験レッスン 1回1000円で実施中
お箏の貸し出し、お箏屋さん紹介します!
サイズ
A4
ページ数
片面
希望イメージ
シンプル 複雑
単色 カラフル
暗い 明るい
日常 高級
遊び心 厳粛
未来的 伝統的
女性的 男性的
希望する色
赤系
納品ファイル
• 高解像度JPG (.jpg)
補足説明
お気に入りの宣材写真を何枚か添付しました。
どれを使っていただいても大丈夫です。
一点誤字を見つけました。
プロフィールのところですが
?マークを消してください
よろしくお願いします、、
■ 選んだ理由

初めて見た瞬間に私の好みど真ん中!と思いました。
可愛らしいデザインに本当に惹かれました。
とにかく色味が可愛くて、今風なデザインが好みでした。
私の好みだけで選んで良いのかと悩んだ時もありましたが、
重々しくなく、お箏を習うことのハードルが少しでも下がるような感じがしました。
私の伝えたい内容の優先事項も的確に把握して頂いており、文字を小さくして頂いたり主張を強くしすぎず情報を入れ込んでくださった点も嬉しかったです。

■ 提案者全員のお礼・コメント

この度は沢山のご提案誠にありがとうございました。
正直、こんなに沢山のご提案を頂けると思っておらずとても嬉しかったです。
どのデザインもとても素敵で最後の最後まで本当に悩みました。
予算の関係で全員にお礼が出来ず本当に申し訳ありません。
皆さまからの温かいメッセージは全て拝見させて頂きました。
チラシ作成は私にとっても初めてで、依頼についても至らない点が多々あったかと存じますが、素敵な提案をしていただき、本当にありがとうございました。
またの機会がありましたらぜひよろしくお願いいたします。

```html
<!DOCTYPE html>
<html lang="ja">
<head>
<meta charset="utf-8">
<title>藤堂さやか 箏・三絃教室</title>
<link rel="stylesheet" href="https://fonts.googleapis.com/css2?family=Shippori+Mincho+B1:wght@700;800&family=Zen+Maru+Gothic:wght@500;700;900&display=swap">
<style>
:root{
  --red:#d23a4c;
  --red-deep:#b8283b;
  --pink:#f4bcc6;
  --pink-soft:#fbe3e7;
  --cream:#fff9f6;
  --ink:#4a3a3c;
  --yellow:#fbe9a6;
  --grass:#7e9a52;
}
*{margin:0;padding:0;box-sizing:border-box}
html,body{width:846px;height:1200px;overflow:hidden;background:#fff}
body{font-family:"Zen Maru Gothic",sans-serif;color:var(--ink)}
.flyer{position:relative;width:846px;height:1200px;background:var(--cream);overflow:hidden}

.pattern-top{position:absolute;left:0;top:0;width:846px;height:110px;
  background:linear-gradient(90deg,#f7c6cf,#f09fb0 40%,#f9d3da 70%,#f2a9b8)}
.pattern-right{position:absolute;right:0;top:0;width:120px;height:460px;
  background:linear-gradient(180deg,#f2a9b8,#fbdde3 70%,transparent)}
.hero-photo{position:absolute;left:0;top:60px;width:560px;height:570px;
  background:linear-gradient(180deg,#e9ece0 0%,#c7d3a8 45%,var(--grass) 80%,#6d8845 100%);
  -webkit-mask-image:linear-gradient(90deg,#000 80%,transparent);
  mask-image:linear-gradient(90deg,#000 80%,transparent)}

.title-name{position:absolute;top:80px;right:28px;writing-mode:vertical-rl;
  font-family:"Shippori Mincho B1",serif;font-weight:800;color:var(--red);font-size:30px;letter-spacing:6px;
  background:#fff;padding:14px 6px;border-radius:6px}
.title-main{position:absolute;top:40px;right:96px;writing-mode:vertical-rl;
  font-family:"Shippori Mincho B1",serif;font-weight:800;color:var(--red);font-size:76px;letter-spacing:2px;line-height:1.1}
.title-main rt{font-size:15px;font-family:"Zen Maru Gothic",sans-serif;color:var(--red)}

.tagline{position:absolute;top:90px;left:540px;writing-mode:vertical-rl;font-family:"Shippori Mincho B1",serif;font-weight:700;
  color:var(--red-deep);font-size:25px;line-height:1.55;letter-spacing:3px;text-shadow:0 0 6px #fff,0 0 6px #fff}

.bubble{position:absolute;left:320px;top:390px;width:120px;height:120px;border-radius:50%;background:rgba(255,255,255,.9);
  display:flex;align-items:center;justify-content:center;text-align:center;font-size:12px;font-weight:700;color:var(--red);line-height:1.5;transform:rotate(-8deg)}

.shamisen{position:absolute;left:450px;top:530px;width:80px;height:100px;border-radius:30px 30px 16px 16px;
  background:linear-gradient(160deg,#c48a4a,#8e5a2c 60%,#f3e4cf)}

.profile{position:absolute;left:38px;top:636px;width:395px}
.profile-tag{display:inline-block;background:var(--red);color:#fff;font-size:13px;font-weight:700;padding:3px 10px;border-radius:3px}
.profile-name{font-family:"Shippori Mincho B1",serif;font-weight:800;color:var(--red);font-size:28px;margin:6px 0 10px;letter-spacing:1px;white-space:nowrap}
.profile p{font-size:11.5px;line-height:1.75;font-weight:500}
.profile p + p{margin-top:8px}

.band{background:var(--red);color:#fff;font-weight:900;font-size:22px;padding:4px 14px;border-radius:4px;letter-spacing:2px;white-space:nowrap}
.pill{border:2px solid var(--red);border-radius:4px;font-size:13px;font-weight:700;padding:0 6px;white-space:nowrap;color:var(--red)}

.trial{position:absolute;left:440px;top:650px;width:240px}
.trial-price{display:flex;align-items:baseline;gap:8px;margin-top:8px;color:var(--red);white-space:nowrap}
.trial-price .yen{font-size:36px;font-weight:900}
.trial-price small{font-size:12px;font-weight:700}

.rental{position:absolute;left:696px;top:630px;width:130px;height:130px;border-radius:50%;background:var(--pink-soft);
  border:2px dashed var(--pink);display:flex;align-items:center;justify-content:center;text-align:center;
  font-size:14px;font-weight:700;color:var(--red);line-height:1.5}

.fee{position:absolute;left:440px;top:775px;width:386px}
.fee .band{display:flex;align-items:center;gap:14px}
.fee .band span{font-size:15px;font-weight:700;letter-spacing:0}
.fee-row{display:flex;align-items:center;gap:10px;margin-top:8px;color:var(--red);white-space:nowrap}
.fee-row .yen{font-size:36px;font-weight:900;line-height:1}
.fee-notes{display:flex;flex-direction:column;font-size:11px;line-height:1.3}
.fee-notes small{font-size:11px;font-weight:700}
.fee-notes span{color:var(--ink);font-weight:500}

.classes{position:absolute;left:445px;top:880px;display:flex;gap:14px}
.class-box{width:122px;text-align:center}
.class-name{background:var(--red);color:#fff;font-weight:700;font-size:15px;border-radius:20px;padding:3px 0}
.parking{font-size:10px;font-weight:700;color:var(--red);margin:4px 0}
.map{height:140px;border-radius:6px;background:linear-gradient(135deg,#e9eef3,#d3dde6)}
.addr{font-size:9px;margin-top:6px;line-height:1.4;white-space:nowrap}

.sns{position:absolute;left:716px;top:880px;width:112px;text-align:center}
.sns-head{font-size:11px;font-weight:700;color:var(--red);background:var(--pink-soft);border-radius:12px;padding:3px 0;white-space:nowrap}
.sns-item{margin-top:12px;display:flex;align-items:center;justify-content:center;gap:6px;font-size:13px;font-weight:700;color:var(--red)}
.sns-item i{width:12px;height:12px;background:var(--red);display:inline-block}
.sns-id{font-size:10px;margin-top:4px}

.welcome{position:absolute;left:30px;top:1008px;width:400px;background:var(--yellow);border-radius:8px;padding:6px 12px;
  font-size:15px;font-weight:700;color:var(--red);line-height:1.4;text-align:center}
.contact{position:absolute;left:30px;top:1070px;width:400px;height:80px;background:var(--red);border-radius:10px;color:#fff;
  display:flex;flex-direction:column;justify-content:center;padding-left:20px}
.contact-label{font-size:14px;font-weight:700}
.contact-phone{display:flex;align-items:center;gap:10px;font-size:34px;font-weight:900;letter-spacing:1px}

.pattern-bottom{position:absolute;left:0;bottom:0;width:846px;height:38px;background:linear-gradient(90deg,#f2a9b8,#f9d3da,#f09fb0)}
</style>
</head>
<body>
<main class="flyer">
  <div class="pattern-top" role="img" aria-label="桜と麻の葉の和柄の帯"></div>
  <div class="pattern-right" role="img" aria-label="ピンクの和柄と花の装飾"></div>
  <div class="hero-photo" role="img" aria-label="芝生の上で箏に寄り添い微笑む講師の写真"></div>

  <h1>
    <span class="title-name">藤堂さやか</span>
    <span class="title-main"><ruby>箏<rt>こと</rt></ruby>・<ruby>三絃<rt>さんげん</rt></ruby>教室</span>
  </h1>

  <p class="tagline">和楽器をもっと身近に。<br>沢山の出会いを大切に楽しみに。</p>

  <div class="bubble">楽しくて<br>どなたでも<br>礼儀作法も<br>身につきます！</div>

  <div class="shamisen" role="img" aria-label="三味線のイラスト"></div>

  <section class="profile">
    <span class="profile-tag">講師紹介</span>
    <h2 class="profile-name">藤堂(浅野)さやか</h2>
    <p>埼玉県川越市出身</p>
    <p>桐谷学院中学・高等学校卒業<br>南海芸術大学 音楽学部邦楽科 箏曲生田流専攻卒業</p>
    <p>3歳より箏、16歳より三絃を始める<br>これまでに箏・三絃・十七絃を松田ゆう、村岡千尋子、<br>古畑智代乃の各師に師事</p>
    <p>第25回 若人和楽器コンテスト 優良賞・リスナー賞<br>第4回 北陸古典芸術次世代コンテスト 技能賞</p>
    <p>音楽療法・音楽教育・音楽療育なども勉強中</p>
  </section>

  <section class="trial">
    <div class="band">体験レッスン</div>
    <div class="trial-price"><span class="pill">1回</span><span class="yen">1,000円</span><small>(税込)</small></div>
  </section>
  <div class="rental">お箏の貸し出し、<br>お箏屋さん<br>紹介します！</div>

  <section class="fee">
    <div class="band">料金 <span>お気軽にご相談ください！</span></div>
    <div class="fee-row">
      <span class="pill">月4回/30分</span>
      <span class="yen">8,000円〜</span>
      <span class="fee-notes"><small>(税込)</small><span>※教材費別途</span></span>
    </div>
  </section>

  <div class="classes">
    <div class="class-box">
      <div class="class-name">川越教室</div>
      <div class="parking">駐車場あり</div>
      <div class="map" role="img" aria-label="川越教室の地図"></div>
      <p class="addr">埼玉県川越市柏原台3-7-5</p>
    </div>
    <div class="class-box">
      <div class="class-name">守谷教室</div>
      <div class="parking">駐車場あり</div>
      <div class="map" role="img" aria-label="守谷教室の地図"></div>
      <p class="addr">茨城県守谷市さくら坂5-21-9</p>
    </div>
  </div>

  <aside class="sns">
    <div class="sns-head">SNSにて情報発信中！</div>
    <div class="sns-item"><i></i>TALKU</div>
    <div class="sns-item"><i></i>Pictogram</div>
    <div class="sns-id">sayakakotonote</div>
  </aside>

  <p class="welcome">お子さまからご年配の方まで<br>どなたでもご参加できます♪</p>
  <div class="contact">
    <span class="contact-label">お問い合わせはコチラ</span>
    <span class="contact-phone">
      <svg width="28" height="28" viewBox="0 0 24 24" aria-hidden="true"><path fill="#fff" d="M6.6 10.8a15.1 15.1 0 006.6 6.6l2.2-2.2a1 1 0 011-.25 11.4 11.4 0 003.6.57 1 1 0 011 1V20a1 1 0 01-1 1A17 17 0 013 4a1 1 0 011-1h3.5a1 1 0 011 1c0 1.250.2 2.450.57 3.57a1 1 0 01-.25 1z"/></svg>
      080-3917-2586
    </span>
  </div>

  <div class="pattern-bottom" role="img" aria-label="桜の和柄の帯"></div>
</main>
</body>
</html>
```